Tobin Quartz Portal Page . It's guarantee project!

We need a clean and professional modern web application portal page
That includes the Login & Application Selection screen

Also, I need to design both Desktop and Mobile sizes.
We have an example design for our target

The application is Jetty Schedule and related data.
Our client is a bit conservative.

Theme color preferred : #00508B (main) #DF0D83 (secondary)

Target Market(s)

Oil & Fuel & Gasoline

Number of Pages Required

2 page

Font styles to use
Sans Serif

Colors
0054AA
0677BA
7BADD7
CADEEF
E8F1F8
E54698
E96AAD
F1A4CE
F9D9EA
FCEFF6

Requirements
Must have
• Login Page & Main Screen

```html
<!DOCTYPE html>
<html lang="en">
<head>
<meta charset="utf-8">
<title>Tobin Quartz – Log in</title>
<link rel="stylesheet" href="https://fonts.googleapis.com/css2?family=DM+Sans:wght@400;500;600;700&family=Poppins:wght@400;500&display=swap">
<style>
  :root {
    --navy: #0f2140;
    --brand-blue: #00508b;
    --brand-pink: #df0d83;
    --text-muted: #5b6478;
    --placeholder: #7d8597;
    --field-bg: #ffffff;
    --divider: #c9ccd6;
    --card-bg: rgba(241, 239, 245, 0.9);
    --sky-top: #f3b25a;
    --sky-mid: #c667b8;
    --sky-violet: #7e5aa8;
    --water: #4b3f7e;
    --ground: #1e2a48;
  }
  * { box-sizing: border-box; margin: 0; padding: 0; }
  html, body { width: 1200px; height: 792px; overflow: hidden; }
  body { font-family: "DM Sans", sans-serif; color: var(--navy); background: var(--ground); }

  .screen { position: relative; width: 1200px; height: 792px; overflow: hidden; }

  .hero-photo {
    position: absolute; inset: 0;
    background:
      radial-gradient(ellipse 40% 30% at 8% 4%, rgba(243,178,90,0.9), transparent 70%),
      radial-gradient(ellipse 50% 30% at 85% 10%, rgba(214,110,200,0.75), transparent 70%),
      radial-gradient(ellipse 45% 35% at 72% 72%, rgba(150,160,220,0.35), transparent 70%),
      linear-gradient(180deg, var(--sky-top) 0%, var(--sky-mid) 22%, var(--sky-violet) 38%, var(--water) 55%, var(--ground) 100%);
  }

  .login-card {
    position: absolute; left: 112px; top: 77px;
    width: 490px; height: 638px;
    background: var(--card-bg);
    backdrop-filter: blur(14px);
    border-radius: 8px;
    box-shadow: 0 10px 40px rgba(10, 20, 50, 0.25);
  }
  .login-card > * { position: absolute; left: 67px; }

  .brand-name { top: 51px; font-size: 15px; font-weight: 500; color: var(--brand-pink); }

  .login-title { top: 116px; font-size: 31px; font-weight: 600; letter-spacing: -0.3px; color: var(--navy); }
  .login-subtitle { top: 163px; font-size: 12px; color: var(--text-muted); }

  .sso-button {
    top: 216px; width: 354px; height: 44px;
    display: flex; align-items: center; justify-content: center; gap: 8px;
    background: var(--field-bg); border: none; border-radius: 2px;
    box-shadow: 0 2px 6px rgba(20, 30, 60, 0.12);
    font-family: "DM Sans", sans-serif; font-size: 16px; font-weight: 500; color: var(--navy);
  }
  .sso-dot { width: 15px; height: 15px; border-radius: 50%; background: var(--navy); }

  .divider {
    top: 292px; width: 354px;
    display: flex; align-items: center; gap: 14px;
    font-size: 12px; color: var(--text-muted);
  }
  .divider::before, .divider::after { content: ""; flex: 1; height: 1px; background: var(--divider); }

  .field {
    width: 354px; height: 44px;
    display: flex; align-items: center; gap: 12px;
    padding: 0 17px; background: var(--field-bg); border-radius: 2px;
    font-family: "Poppins", sans-serif; font-size: 13px; color: var(--placeholder);
  }
  .field svg { flex: none; }
  .field-email { top: 334px; }
  .field-password { top: 388px; }
  .field-password .toggle-visibility { margin-left: auto; }

  .options {
    top: 452px; width: 354px;
    display: flex; align-items: center; justify-content: space-between;
    font-family: "Poppins", sans-serif; font-size: 12px;
  }
  .remember { display: flex; align-items: center; gap: 9px; color: var(--placeholder); }
  .checkbox { width: 19px; height: 19px; border-radius: 3px; background: var(--brand-blue); display: grid; place-items: center; }
  .forgot-link { color: var(--brand-blue); font-weight: 500; text-decoration: none; }

  .login-button {
    top: 505px; width: 354px; height: 44px;
    background: var(--brand-pink); color: #fff; border: none; border-radius: 2px;
    font-family: "DM Sans", sans-serif; font-size: 14px; font-weight: 600;
  }

  .signup-prompt {
    top: 570px; left: 0; width: 100%; text-align: center;
    font-size: 11.5px; color: var(--text-muted);
  }
  .signup-prompt a { color: var(--brand-blue); font-weight: 600; text-decoration: none; margin-left: 4px; }
</style>
</head>
<body>
<main class="screen">
  <div class="hero-photo" role="img" aria-label="Aerial photo of an oil terminal with storage tanks and a lit pier along the water at sunset"></div>

  <section class="login-card">
    <div class="brand-name">Tobin Quartz</div>
    <h1 class="login-title">Log in to your Account</h1>
    <p class="login-subtitle">Welcome back! Select method to log in:</p>

    <button class="sso-button"><span class="sso-dot"></span>Orbitly</button>

    <div class="divider">or continue with email</div>

    <label class="field field-email">
      <svg width="15" height="12" viewBox="0 0 15 12" fill="none" stroke="#7d8597" stroke-width="1.3"><rect x="0.7" y="0.7" width="13.6" height="10.6" rx="1"/><path d="M1 1.5l6.5 5 6.5-5"/></svg>
      Email address
    </label>

    <label class="field field-password">
      <svg width="13" height="15" viewBox="0 0 13 15" fill="none" stroke="#7d8597" stroke-width="1.3"><rect x="0.7" y="6" width="11.6" height="8.3" rx="1.5"/><path d="M3.2 6V4a3.3 3.3 0 016.6 0v2"/><circle cx="6.5" cy="10" r="0.9" fill="#7d8597"/></svg>
      Password
      <svg class="toggle-visibility" width="17" height="14" viewBox="0 0 17 14" fill="none" stroke="#0f2140" stroke-width="1.4"><path d="M1 7s2.8-5 7.5-5S16 7 16 7s-2.8 5-7.5 5S1 7 1 7z"/><circle cx="8.5" cy="7" r="2.3"/><path d="M2 1l13 12"/></svg>
    </label>

    <div class="options">
      <span class="remember">
        <span class="checkbox"><svg width="10" height="8" viewBox="0 0 10 8" fill="none" stroke="#fff" stroke-width="1.6"><path d="M1 4l2.8 2.8L9 1"/></svg></span>
        Remember Me
      </span>
      <a class="forgot-link" href="#">Forgot Passworld?</a>
    </div>

    <button class="login-button">Log In</button>

    <p class="signup-prompt">Don’t have an account?<a href="#">Create an account</a></p>
  </section>
</main>
</body>
</html>
```